Modern Business Card

Modern professional business card with more than just logo and demographic info. Something memorable.

We are a trendy/modern chiropractic group with an emphasis on neurology, hence the minimalist-type brain logo. We want to convey that modern and technical aspect with professionalism and the elite nature of our practice environment.

```html
<!DOCTYPE html>
<html lang="en">
<head>
<meta charset="utf-8">
<title>Meridian Chiropractic – Business Card</title>
<link rel="stylesheet" href="https://fonts.googleapis.com/css2?family=Raleway:wght@700&family=Arimo:wght@400;700&family=Cinzel:wght@400&display=swap">
<style>
  :root {
    --backdrop: #7b4a2b;
    --kraft-light: #d9b88f;
    --kraft-mid: #c39a6c;
    --kraft-dark: #a97b4f;
    --ink: #111111;
    --card-shadow: rgba(0, 0, 0, 0.45);
  }
  * { box-sizing: border-box; margin: 0; padding: 0; }
  html, body {
    width: 1200px;
    height: 900px;
    overflow: hidden;
    background: var(--backdrop);
  }
  .canvas {
    position: relative;
    width: 1200px;
    height: 900px;
  }
  .card {
    position: absolute;
    left: 330px;
    width: 556px;
    height: 343px;
    background: linear-gradient(160deg, var(--kraft-light) 0%, var(--kraft-mid) 55%, var(--kraft-dark) 100%);
    box-shadow: 2px 4px 8px var(--card-shadow);
    color: var(--ink);
  }
  .card--back { top: 90px; }
  .card--front { top: 470px; }

  .contact {
    position: absolute;
    top: 66px;
    left: 0;
    width: 100%;
    text-align: center;
    font-family: "Arimo", Arial, sans-serif;
    font-size: 16px;
    line-height: 20px;
  }
  .contact__name {
    font-family: "Raleway", sans-serif;
    font-weight: 700;
    font-size: 20px;
    line-height: 22px;
    letter-spacing: 0.5px;
  }
  .contact__title { line-height: 18px; }
  .contact__rule {
    width: 136px;
    height: 1px;
    background: var(--ink);
    margin: 11px auto 12px;
  }
  .contact__label { font-weight: 700; }
  .contact__rule--lower { margin: 12px auto 16px; }

  .brand {
    position: absolute;
    top: 124px;
    left: 113px;
    display: flex;
    align-items: center;
    gap: 16px;
  }
  .brand__dot {
    width: 70px;
    height: 70px;
    border-radius: 50%;
    background: var(--ink);
  }
  .brand__name {
    font-family: "Cinzel", serif;
    font-weight: 400;
    color: var(--ink);
    line-height: 1;
  }
  .brand__name-main {
    display: block;
    font-size: 50px;
    letter-spacing: 1px;
  }
  .brand__name-sub {
    display: block;
    font-size: 22px;
    letter-spacing: 0.5px;
    margin-top: 2px;
  }
</style>
</head>
<body>
  <main class="canvas">
    <section class="card card--back" aria-label="Contact side">
      <div class="contact">
        <p class="contact__name">DANIEL CARTER</p>
        <p class="contact__title">Managing Director</p>
        <div class="contact__rule"></div>
        <p><span class="contact__label">P:</span> 044-123 456 789</p>
        <p><span class="contact__label">M:</span> 044-123 456 789</p>
        <p><span class="contact__label">E:</span> info@webname.com</p>
        <p><span class="contact__label">W:</span> www.websitename.com</p>
        <div class="contact__rule contact__rule--lower"></div>
        <p>12345, Address Goes Here</p>
        <p>Country Name, 123456.</p>
      </div>
    </section>

    <section class="card card--front" aria-label="Brand side">
      <div class="brand">
        <span class="brand__dot" aria-hidden="true"></span>
        <p class="brand__name">
          <span class="brand__name-main">MERIDIAN</span>
          <span class="brand__name-sub">CHIROPRACTIC</span>
        </p>
      </div>
    </section>
  </main>
</body>
</html>
```